Design Our Holiday Magic Coupon

Purpose - The purpose of this project is to create a festive, uplifting, and visually engaging physical coupon that will be mailed to our existing community and warm leads.
The intent is twofold: first, to spark delight and connection by offering a tangible, personal touch during the holiday season; and second, to encourage customers to explore and purchase our programs as they prepare for a strong start to 2026. This mailer is designed to re-engage past buyers, inspire current participants, and gently invite new momentum into their practice through a simple, friendly offer.

Project Description + Scope

This project includes the design and production of a printed coupon ( card format) featuring a 20% discount on purchases of $79 or more. The copy should feel warm, clear, and celebratory without urgency or pressure.

The front of the card will include the headline (“Live Your Best 2026”), bold discount information, and the coupon code JOLLYDAY20. The back will include a short message reinforcing the tone of possibility and ease, plus simple redemption instructions and the expiry date: December 31, 2025. Deliverables include print-ready artwork, color selection aligned with KH brand style.

one side
LIVE YOUR BEST 2026
Enjoy 20% OFF when you buy $79 or more.
Use code: JOLLYDAY20
Redeem until end of day December 31, 2025.

Back side - Move with clarity.
Heal with intelligence.
Lead with ease.
Thank you for being part of Kinetic Harmony.
Lots of love, Marla and the whole of Team Marla

Target Market(s)

yoga teachers, yoga lovers, mostly over 50 years, women

Font styles to use
Other font styles liked:
• see attached for feel

Colors
0054AA
0677BA
7BADD7
CADEEF
E8F1F8
0094D4
00A9DD
6FCCEA
C7EBF8
E9F6FB
00AB8E
00BBA5
67D7C9
C6EFE9
E9F9F6
EB3D1F
EC4F4E
F09395
F8D3D4
FCEDEE

Requirements
Nice to have
• see attached

```html
<!DOCTYPE html>
<html lang="en">
<head>
<meta charset="utf-8">
<title>Kinetic Harmony – Holiday Coupon</title>
<link rel="stylesheet" href="https://fonts.googleapis.com/css2?family=Cinzel:wght@600;700&family=Montserrat:wght@300;400;500;700&display=swap">
<style>
  :root {
    --backdrop: #3e434f;
    --sky-light: #dcf8fc;
    --sky-mid: #9bedfb;
    --sky-deep: #33defc;
    --ink-teal: #1f88a8;
    --white: #ffffff;
    --panel: rgba(255, 255, 255, 0.78);
    --wave-teal: #6fdbe6;
    --wave-green: #7fd38a;
    --wave-lime: #cfe9a6;
  }
  * { margin: 0; padding: 0; box-sizing: border-box; }
  html, body {
    width: 1200px; height: 1037px; overflow: hidden;
    background: var(--backdrop);
  }
  .card {
    position: absolute; left: 181px; width: 839px; height: 419px;
    overflow: hidden;
    background: linear-gradient(200deg, var(--sky-deep) 0%, var(--sky-mid) 45%, var(--sky-light) 100%);
    font-family: 'Montserrat', sans-serif;
  }
  .card--front { top: 82px; }
  .card--back { top: 535px; }
  .card__waves { position: absolute; inset: 0; width: 100%; height: 100%; }

  /* front */
  .brand-name {
    position: absolute; left: 70px; top: 104px; width: 240px; text-align: center;
    font-family: 'Montserrat', sans-serif; font-weight: 300; font-size: 26px;
    color: var(--white); letter-spacing: 0.5px;
  }
  .brand-dot {
    position: absolute; left: 176px; top: 48px; width: 34px; height: 34px;
    border-radius: 50%; background: var(--white);
  }
  .divider {
    position: absolute; left: 319px; top: 21px; width: 1.5px; height: 139px;
    background: var(--white);
  }
  .headline-small {
    position: absolute; left: 346px; top: 26px;
    font-weight: 700; font-size: 38px; line-height: 45px; color: var(--white);
  }
  .headline-year {
    position: absolute; left: 466px; top: 22px;
    font-weight: 700; font-size: 118px; line-height: 134px; color: var(--white);
    letter-spacing: -1px;
  }
  .enjoy {
    position: absolute; left: 22px; top: 158px;
    font-weight: 500; font-size: 27px; line-height: 32px; color: var(--ink-teal);
  }
  .discount {
    position: absolute; left: 22px; top: 192px;
    font-family: 'Cinzel', serif; font-weight: 600; color: var(--ink-teal);
    white-space: nowrap; line-height: 1;
  }
  .discount__value { font-size: 118px; letter-spacing: -4px; }
  .discount__off { font-size: 58px; font-weight: 700; margin-left: 8px; }
  .condition {
    position: absolute; left: 403px; top: 232px; width: 412px; height: 56px;
    background: var(--panel);
    display: flex; align-items: center; justify-content: center;
    font-weight: 500; font-size: 26px; color: var(--ink-teal); white-space: nowrap;
  }
  .condition strong { font-weight: 700; }
  .code-label {
    position: absolute; left: 310px; top: 357px;
    font-weight: 500; font-size: 18px; color: var(--white);
  }
  .code-box {
    position: absolute; left: 403px; top: 307px; width: 268px; height: 79px;
    background: var(--panel); padding: 12px;
  }
  .code-box__inner {
    width: 100%; height: 100%; border: 1.5px dashed var(--ink-teal);
    display: flex; align-items: center; justify-content: center;
    font-family: 'Cinzel', serif; font-weight: 700; font-size: 34px;
    color: var(--ink-teal); letter-spacing: -1px;
  }
  .expiry {
    position: absolute; left: 401px; top: 391px;
    font-weight: 500; font-size: 12px; color: var(--ink-teal); white-space: nowrap;
  }

  /* back */
  .mantra { position: absolute; left: 0; width: 100%; text-align: center; white-space: nowrap; }
  .mantra--sans {
    font-weight: 700; font-size: 36px; color: var(--white); letter-spacing: 1px;
  }
  .mantra--serif {
    font-family: 'Cinzel', serif; font-weight: 700; font-size: 42px;
    color: var(--ink-teal); top: 86px;
  }
  .mantra--one { top: 38px; }
  .mantra--three { top: 137px; }
  .thanks {
    position: absolute; left: 171px; top: 201px; width: 472px; height: 160px;
    background: rgba(255, 255, 255, 0.6);
    display: flex; flex-direction: column; justify-content: center; align-items: center;
    font-family: 'Cinzel', serif; font-weight: 700; font-size: 24.5px; line-height: 29px;
    color: var(--ink-teal); text-align: center; white-space: nowrap;
  }
  .site {
    position: absolute; left: 0; top: 376px; width: 100%; text-align: center;
    font-weight: 500; font-size: 19.5px; letter-spacing: 2px; color: var(--ink-teal);
  }
</style>
</head>
<body>

<section class="card card--front" aria-label="Coupon front">
  <svg class="card__waves" viewBox="0 0 839 419" preserveAspectRatio="none" aria-hidden="true">
    <path d="M0 315 C120 290 260 300 400 340 C520 375 700 360 839 330 L839 419 L0 419 Z" fill="var(--wave-teal)" opacity="0.55"/>
    <path d="M0 365 C140 350 260 380 360 410 L0 419 Z" fill="var(--wave-lime)" opacity="0.9"/>
    <path d="M130 419 C220 360 330 340 430 345 C560 352 700 390 839 400 L839 419 Z" fill="var(--wave-green)" opacity="0.7"/>
    <path d="M0 312 C150 290 300 305 420 352" fill="none" stroke="#3fb7c9" stroke-width="1.5" opacity="0.7"/>
    <path d="M839 150 C700 190 560 240 420 300 C600 260 720 230 839 200 Z" fill="#ffffff" opacity="0.15"/>
  </svg>

  <span class="brand-dot" aria-hidden="true"></span>
  <div class="brand-name">kinetic harmony</div>
  <span class="divider" aria-hidden="true"></span>

  <div class="headline-small">LIVE<br>YOUR<br>BEST</div>
  <div class="headline-year">2026</div>

  <div class="enjoy">Enjoy</div>
  <div class="discount"><span class="discount__value">20%</span><span class="discount__off">OFF</span></div>

  <div class="condition">when you buy&nbsp;<strong>$79</strong>&nbsp;or more.</div>

  <div class="code-label">Use code:</div>
  <div class="code-box"><div class="code-box__inner">JOLLYDAY20</div></div>
  <div class="expiry">Redeem until end of day December 31, 2025</div>
</section>

<section class="card card--back" aria-label="Coupon back">
  <svg class="card__waves" viewBox="0 0 839 419" preserveAspectRatio="none" aria-hidden="true">
    <path d="M0 315 C120 290 260 300 400 340 C520 375 700 360 839 330 L839 419 L0 419 Z" fill="var(--wave-teal)" opacity="0.55"/>
    <path d="M0 365 C140 350 260 380 360 410 L0 419 Z" fill="var(--wave-lime)" opacity="0.9"/>
    <path d="M130 419 C220 360 330 340 430 345 C560 352 700 390 839 400 L839 419 Z" fill="var(--wave-green)" opacity="0.7"/>
    <path d="M0 312 C150 290 300 305 420 352" fill="none" stroke="#3fb7c9" stroke-width="1.5" opacity="0.7"/>
    <path d="M839 150 C700 190 560 240 420 300 C600 260 720 230 839 200 Z" fill="#ffffff" opacity="0.15"/>
  </svg>

  <div class="mantra mantra--sans mantra--one">MOVE WITH CLARITY.</div>
  <div class="mantra mantra--serif">HEAL WITH INTELLIGENCE.</div>
  <div class="mantra mantra--sans mantra--three">LEAD WITH EASE.</div>

  <div class="thanks">
    <p>THANK YOU FOR BEING PART OF</p>
    <p>KINETIC HARMONY.</p>
    <p>LOTS OF LOVE, MARLA</p>
    <p>AND THE WHOLE OF TEAM MARLA</p>
  </div>

  <div class="site">kineticharmonyflow.com</div>
</section>

</body>
</html>
```